Vibrant business card design for Product person in Tech

I'm a 29 y/o female Product manager and I'd like to get a business card designed I can use when networking. I'd love something that stands out. Feel free to experiment with the use of colour, maybe geometrical elements - get creative! I work in the tech industry, so looking for a design without too much of a corporate feel. <br/><br/>The business card should have room for:<br/>Name<br/>Email address<br/>Linkora

Target Market(s)

Tech

Contact Information for Business Card

Name
Email
Linkora

Colors
faa54b
00a990
33b8a4
abd037
fbee3f
e667a6
ffcf3e
f59195

```html
<!DOCTYPE html>
<html lang="en">
<head>
<meta charset="utf-8">
<title>Business Card – Product Manager</title>
<link rel="stylesheet" href="https://fonts.googleapis.com/css2?family=Arimo:wght@700&display=swap">
<style>
  :root {
    --backdrop: #4b4b4b;
    --pink: #e667a6;
    --teal: #00a990;
    --teal-light: #33b8a4;
    --orange: #faa54b;
    --lime: #abd037;
    --white: #ffffff;
    --ink: #333333;
  }
  html, body {
    margin: 0;
    padding: 0;
    width: 1200px;
    height: 1200px;
    overflow: hidden;
    background: var(--backdrop);
  }
  .canvas {
    display: block;
    width: 1200px;
    height: 1200px;
  }
  .card-text {
    font-family: "Arimo", Arial, sans-serif;
    font-weight: 700;
    fill: var(--ink);
  }
  .pink { fill: var(--pink); }
  .teal { fill: var(--teal); }
  .teal-light { fill: var(--teal-light); }
  .orange { fill: var(--orange); }
  .lime { fill: var(--lime); }
  .white { fill: var(--white); }
</style>
</head>
<body>
<svg class="canvas" viewBox="0 0 1932 1932" xmlns="http://www.w3.org/2000/svg">
  <rect class="backdrop" width="1932" height="1932" fill="var(--backdrop)"/>

  <!-- Front of card -->
  <g class="card-front">
    <rect class="pink" x="315" y="180" width="1342" height="766" role="img" aria-label="Pink background with a grid pattern of rounded squares"/>
    <polygon class="white" points="510,214 1108,214 1108,392"/>
    <polygon class="teal" points="315,180 1657,593 315,946"/>
    <polygon class="orange" points="466,371 1657,593 315,946"/>
    <polygon class="lime" points="560,490 1657,593 315,946"/>
    <polygon class="white" points="315,946 1657,593 1330,946"/>
    <polygon class="lime" points="1330,946 1657,593 1467,946"/>
    <polygon class="teal-light" points="1467,946 1657,593 1565,946"/>
    <polygon class="orange" points="1565,946 1657,593 1657,946"/>

    <g class="contact-panel">
      <polygon class="lime" points="1125,214 1615,214 1615,547 1125,398"/>
      <text class="card-text name" x="1362" y="288" font-size="48" text-anchor="middle">YOUR NAME</text>
      <text class="card-text email" x="1366" y="360" font-size="28" text-anchor="middle">your.email@company.com</text>
      <text class="card-text profile" x="1553" y="437" font-size="32" text-anchor="end">Linkora</text>
    </g>
  </g>

  <!-- Back of card -->
  <rect class="card-back pink" x="315" y="995" width="1342" height="767"/>
</svg>
</body>
</html>
```